Propose a revamped landing page

One template we like eg is https://www.tornavo.com but but cluttered Our logo and colors are attached to our logo and colors are printed on a white background what we have. So font usage ...
Number of Pages Required
1 page

```html
<!DOCTYPE html>
<html lang="en">
<head>
<meta charset="utf-8">
<title>Skyvane — Cloud services</title>
<link href="https://fonts.googleapis.com/css2?family=Montserrat:wght@400;500;600;800&display=swap" rel="stylesheet">
<style>
  :root {
    --ink: #1f2533;
    --muted: #8a93a6;
    --accent: #00c2ff;
    --accent-deep: #0a6ef0;
    --pale: #e6f0ff;
    --pale-soft: #f2f7ff;
    --warm: #ffc46b;
    --white: #ffffff;
  }
  * { box-sizing: border-box; margin: 0; padding: 0; }
  html, body { width: 1200px; height: 1200px; overflow: hidden; background: var(--white); }
  body { position: relative; font-family: "Montserrat", sans-serif; color: var(--ink); }

  .topbar { position: absolute; left: 416px; top: 5px; width: 436px; display: flex; justify-content: space-between; font-size: 8px; color: var(--muted); }
  .topbar nav { display: flex; gap: 14px; }
  .header { position: absolute; left: 416px; top: 40px; width: 436px; display: flex; align-items: center; justify-content: space-between; }
  .brand { font-weight: 800; font-size: 16px; color: var(--ink); }
  .header-menu { font-size: 8px; color: var(--muted); }
  .header-login { font-size: 8px; color: var(--muted); }

  .promo-bar { position: absolute; left: 416px; top: 72px; width: 436px; height: 28px; border-radius: 8px; background: var(--accent); color: var(--white); font-size: 9px; font-weight: 600; display: flex; align-items: center; padding: 0 18px; }

  .hero-title { position: absolute; left: 416px; top: 134px; width: 260px; font-size: 27px; line-height: 32px; font-weight: 800; }
  .hero-features { position: absolute; left: 416px; top: 222px; display: flex; gap: 30px; }
  .feature { width: 108px; padding-left: 10px; border-left: 3px solid var(--warm); font-size: 8px; line-height: 12px; color: var(--muted); }
  .hero-art { position: absolute; left: 704px; top: 118px; width: 236px; height: 222px; border-radius: 24px;
    background: radial-gradient(circle at 40% 45%, #2a8cff 0 22%, #bfe0ff 40%, var(--pale-soft) 70%, var(--white) 100%); }

  .btn { position: absolute; height: 24px; border-radius: 12px; background: var(--pale); color: var(--accent-deep); font-size: 8px; font-weight: 600; display: flex; align-items: center; justify-content: center; box-shadow: 0 4px 10px rgba(0,150,255,.15); }
  .btn-hero { left: 416px; top: 288px; width: 96px; }

  .cloud-band { position: absolute; left: 328px; top: 344px; width: 612px; height: 428px; }
  .cloud-art { position: absolute; left: 328px; top: 376px; width: 272px; height: 272px; background: linear-gradient(150deg, #1aa7ff 0%, #6fd0ff 30%, var(--pale-soft) 65%, var(--white) 100%); }

  .section-title { position: absolute; font-size: 30px; line-height: 33px; font-weight: 800; }
  .title-cloud { left: 628px; top: 390px; }
  .title-next { left: 416px; top: 810px; }

  .spec-list { position: absolute; list-style: none; font-size: 8px; line-height: 11px; color: var(--muted); }
  .spec-list li { margin-bottom: 12px; padding-left: 8px; position: relative; }
  .spec-list li::before { content: ""; position: absolute; left: 0; top: 4px; width: 3px; height: 3px; border-radius: 50%; background: var(--accent); }
  .spec-list strong { color: var(--ink); font-weight: 600; }
  .list-cloud { left: 638px; top: 478px; width: 200px; }
  .list-next { left: 426px; top: 904px; width: 200px; }

  .btn-cloud { left: 632px; top: 700px; width: 88px; }
  .btn-next { left: 416px; top: 1128px; width: 92px; }
</style>
</head>
<body>
  <div class="topbar">
    <nav><span>Home</span><span>About</span><span>Blog</span><span>Help</span></nav>
    <span>Contact us</span>
  </div>

  <header class="header">
    <div class="brand">Skyvane</div>
    <div class="header-menu">Our solutions</div>
    <div class="header-login">Log in</div>
  </header>

  <div class="promo-bar">Try cloud hosting free for 30 days — no card needed</div>

  <h1 class="hero-title">Your SaaS partner in cloud services</h1>
  <div class="hero-features">
    <p class="feature">Fast, secure cloud storage</p>
    <p class="feature">Support around the clock every day</p>
  </div>
  <a class="btn btn-hero">Learn more</a>
  <div class="hero-art" role="img" aria-label="Isometric illustration of a phone and cloud data icons"></div>

  <svg class="cloud-band" viewBox="0 0 612 428" aria-hidden="true">
    <path d="M0 0 H420 C470 0 500 60 612 64 V428 H216 C190 428 180 370 120 350 C60 330 20 330 0 330 Z" fill="var(--pale)"/>
  </svg>
  <div class="cloud-art" role="img" aria-label="Isometric illustration of a server screen over a network grid"></div>

  <h2 class="section-title title-cloud">CloUD<br>Technology</h2>
  <ul class="spec-list list-cloud">
    <li><strong>Global network</strong> of data centers</li>
    <li>99.9% uptime</li>
    <li>Daily backups</li>
    <li>24/7 monitoring</li>
    <li><strong>Auto scaling</strong> for peak traffic</li>
    <li><strong>Single sign-on</strong> for teams</li>
    <li>Migrate your current stack in minutes with our team</li>
  </ul>
  <a class="btn btn-cloud">Learn more</a>

  <h2 class="section-title title-next">NextGen<br>Technology</h2>
  <ul class="spec-list list-next">
    <li><strong>Global network</strong> of data centers</li>
    <li>99.9% uptime</li>
    <li>Daily backups</li>
    <li>24/7 monitoring</li>
    <li><strong>Auto scaling</strong> for peak traffic</li>
    <li><strong>Single sign-on</strong> for teams</li>
    <li>Migrate your current stack in minutes with our team</li>
  </ul>
  <a class="btn btn-next">Learn more</a>
</body>
</html>
```